THE TALL COPPER ATLAS OF PORTS

subtitle: AN INTRO TO SEARCH ENGINE OPTIMIZATION
background: white
dimensions: 1562x2500

Target Market(s)

Marketing professionals

Industry/Entity Type

Digital Marketing

Font styles to use
Sans Serif

Colors
ffffff
1b1b1b
3176b5

Requirements
Should not have
• Images or graphics

```html
<!DOCTYPE html>
<html lang="en">
<head>
<meta charset="utf-8">
<title>The Tall Copper Atlas of Ports</title>
<link rel="stylesheet" href="https://fonts.googleapis.com/css2?family=Anton&family=Oswald:wght@500;600&family=Open+Sans&display=swap">
<style>
  :root {
    --paper: #ffffff;
    --ink: #1b1b1b;
    --brand-blue: #3176b5;
    --rule-grey: #8a8a8a;
    --field-grey: #eaeceb;
    --field-border: #e2e2e2;
    --button-blue: #b3cbe4;
    --muted: #6d6d6d;
  }
  html, body {
    margin: 0;
    padding: 0;
    overflow: hidden;
    background: var(--paper);
  }
  .cover {
    position: relative;
    width: 750px;
    height: 1200px;
    overflow: hidden;
    background: var(--paper);
  }
  .title-block {
    position: absolute;
    left: 0;
    top: 0;
    width: 750px;
    height: 860px;
  }
  .title-line {
    font-family: "Oswald", sans-serif;
    font-weight: 600;
    fill: var(--brand-blue);
  }
  .title-keyword {
    font-family: "Anton", sans-serif;
    fill: var(--brand-blue);
  }
  .title-rule {
    fill: var(--rule-grey);
  }
  .tagline {
    font-family: "Oswald", sans-serif;
    font-weight: 500;
    fill: var(--ink);
  }
  .search-bar {
    position: absolute;
    left: 166px;
    top: 954px;
    width: 418px;
    height: 40px;
    border: 1px solid var(--field-border);
    border-radius: 3px;
    background: var(--paper);
    padding: 2px;
    display: flex;
  }
  .search-field {
    flex: 1;
    display: flex;
    align-items: center;
    background: var(--field-grey);
    border-radius: 2px 0 0 2px;
    font-family: "Open Sans", sans-serif;
    font-size: 17px;
    color: var(--muted);
  }
  .search-icon {
    width: 32px;
    height: 32px;
    margin: 0 10px 0 12px;
  }
  .search-button {
    width: 82px;
    display: flex;
    align-items: center;
    justify-content: center;
    background: var(--button-blue);
    border-radius: 3px;
    font-family: "Open Sans", sans-serif;
    font-size: 17px;
    color: var(--muted);
  }
  .author {
    position: absolute;
    left: 0;
    top: 1096px;
    width: 750px;
    margin: 0;
    text-align: center;
    font-family: "Oswald", sans-serif;
    font-weight: 500;
    font-size: 44px;
    line-height: 60px;
    color: var(--brand-blue);
  }
</style>
</head>
<body>
  <main class="cover">
    <svg class="title-block" viewBox="0 0 750 860" aria-labelledby="book-title">
      <title id="book-title">The Tall Copper Atlas of Ports</title>
      <text class="title-line" x="68" y="176" font-size="136" textLength="378" lengthAdjust="spacingAndGlyphs">The Tall</text>
      <rect class="title-rule" x="68" y="195" width="611" height="3"/>
      <text class="title-line" x="68" y="324" font-size="136" textLength="612" lengthAdjust="spacingAndGlyphs">Copper Atlas of</text>
      <rect class="title-rule" x="68" y="341" width="611" height="3"/>
      <text class="title-keyword" x="68" y="776" font-size="478" textLength="612" lengthAdjust="spacingAndGlyphs">PORTS</text>
      <rect class="title-rule" x="68" y="795" width="611" height="3"/>
      <text class="tagline" x="68" y="838" font-size="31" textLength="616" lengthAdjust="spacingAndGlyphs">Logic between the search engine, and the searcher...</text>
    </svg>

    <div class="search-bar">
      <div class="search-field">
        <svg class="search-icon" viewBox="0 0 32 32" aria-hidden="true">
          <circle cx="13" cy="13" r="9" fill="none" stroke="#9a9a9a" stroke-width="3"/>
          <line x1="19.5" y1="19.5" x2="28" y2="28" stroke="#9a9a9a" stroke-width="4" stroke-linecap="round"/>
        </svg>
        <span>www.</span>
      </div>
      <div class="search-button">Search</div>
    </div>

    <p class="author">Author Name</p>
  </main>
</body>
</html>
```